Compelling Home Page for Clip Harbor Partners

We are a Video SEO specialist that get websites on top of the front page of Zentrova and FlickBarn with video thumbprints that generate great traffic. Video SEO is all we do

see what we're offering at a salespage www.plumfieldreels.example. However, please omit "guarantee"

he home page should introduce our company as a premier company for helping brands get their videos on the front page of zentrova and high up in flickbarn. Should incorporate video "thumbnails" as part of the design. These could be the "triangular click buttons" or little video screens you see as "thumbnails" Needs a prominent place for a video about videoSEO. on Left side of page towards the top.

Needs buttons across the top for other pages. See www.brastonclips.example for frame of reference we want to be better than them.

Must incorporate our logo. We'd like to see the logo on dark background as well as white background.

Simple but with bright and vibrant highlights that look sophisticated, cutting edge and accountable. Shows credentials. Links with examples of thumbnails that are on the front page

We want to beat www.brastonclips.example check it out for point of reference

Target Market(s)

large corporations who have videos already and want to get better traction. Marlow 500. Advertising Agencies for Marlow 500's

Requirements
Must have
• Incorporate our logo. clean, easy to read

```html
<!DOCTYPE html>
<html lang="en">
<head>
<meta charset="utf-8">
<title>Clip Harbor Partners — Video SEO</title>
<link href="https://fonts.googleapis.com/css2?family=Crimson+Text:wght@400;600&family=Cinzel:wght@400&display=swap" rel="stylesheet">
<style>
  :root {
    --ink: #000000;
    --paper: #ffffff;
    --blue: #1f86f0;
    --blue-deep: #0b4fb8;
    --blue-light: #5fb0ff;
    --gold: #ffcc00;
    --text: #ffffff;
    --muted: #cfcfcf;
    --dark-text: #111111;
  }
  * { box-sizing: border-box; margin: 0; padding: 0; }
  html, body { width: 1113px; height: 1200px; overflow: hidden; background: var(--ink); }
  body { font-family: "Crimson Text", Georgia, serif; color: var(--text); position: relative; }
  .page { position: relative; width: 1113px; height: 1200px; background: var(--ink); overflow: hidden; }

  .brand { position: absolute; display: flex; align-items: center; gap: 8px; font-family: "Crimson Text", serif; font-weight: 600; }
  .brand-mark { width: 22px; height: 22px; border-radius: 50%; background: var(--blue); }
  .brand--dark { left: 38px; top: 38px; color: var(--paper); font-size: 19px; }
  .brand--light { left: 28px; top: 990px; color: var(--dark-text); font-size: 16px; }

  .nav-band { position: absolute; left: 0; top: 85px; width: 1113px; height: 50px;
    background: linear-gradient(var(--blue-light), var(--blue) 40%, var(--blue-deep));
    border-top: 2px solid #d9ecff; border-bottom: 2px solid #9fc9f5; }
  .nav-item { position: absolute; top: 72px; width: 76px; height: 76px; border-radius: 50%;
    background: radial-gradient(circle at 50% 30%, #4fa8ff, #0a5fd0 55%, #052d7a);
    box-shadow: 0 0 6px #000 inset, 0 3px 6px rgba(0,0,0,.6);
    display: flex; align-items: center; justify-content: center;
    color: var(--gold); font-size: 18px; text-decoration: none; white-space: nowrap; }

  .video-player { position: absolute; left: 63px; top: 210px; width: 233px; height: 162px;
    background: var(--ink); border: 4px solid #e9e9e9; }
  .video-player .controls { position: absolute; left: 0; bottom: 0; width: 100%; height: 14px; background: #d8d8d8; }

  .search-showcase { position: absolute; left: 733px; top: 187px; width: 367px; height: 226px;
    background: linear-gradient(100deg, #f4f4f7 0%, #e6e8f4 55%, #cfd3e6 100%);
    box-shadow: -40px -20px 80px rgba(255,255,255,.25); }

  .tagline { position: absolute; left: 54px; top: 408px; font-family: "Cinzel", serif; font-size: 25px; letter-spacing: 3px; }
  .subhead { position: absolute; left: 52px; top: 458px; font-size: 22px; }
  .gold { color: var(--gold); }
  .intro { position: absolute; left: 53px; top: 489px; width: 715px; font-size: 16.4px; line-height: 19px; }
  .rule { position: absolute; left: 53px; top: 609px; width: 713px; border-top: 1px dashed #666; }

  .benefits { position: absolute; top: 623px; width: 420px; }
  .benefits h2 { font-weight: 400; font-size: 18.5px; margin-bottom: 8px; }
  .benefits ul { list-style: none; font-size: 16.4px; line-height: 19px; }
  .benefits li { position: relative; padding-left: 12px; margin-bottom: 17px; }
  .benefits li::before { content: ""; position: absolute; left: 0; top: 7px; width: 6px; height: 6px; border-radius: 50%; background: var(--blue); }
  .benefits--left { left: 52px; }
  .benefits--right { left: 484px; }
  .divider { position: absolute; left: 466px; top: 661px; height: 139px; border-left: 1px solid #777; }

  .client-tile { position: absolute; top: 853px; width: 139px; height: 106px; background: var(--paper);
    border: 5px solid #d9d9d9; border-radius: 4px; display: flex; align-items: center; justify-content: center;
    color: var(--dark-text); font-size: 24px; font-weight: 600; }

  .cta-band { position: absolute; left: 0; top: 976px; width: 1113px; height: 58px; background: var(--paper); }
  .cta { position: absolute; left: 372px; top: 990px; display: flex; align-items: center; gap: 10px; color: var(--dark-text); font-size: 17px; }

  .footer { position: absolute; left: 0; top: 1034px; width: 1113px; height: 166px;
    background: linear-gradient(var(--blue) 0%, #1573e0 60%, #0f5cc6 100%); }
  .partner-list { position: absolute; left: 30px; top: 50px; display: grid; grid-template-columns: repeat(3, 70px); gap: 16px 4px; color: var(--ink); font-size: 13px; font-weight: 600; }
  .footer-nav { position: absolute; left: 372px; top: 52px; display: flex; gap: 19px; font-size: 17px; }
  .footer-nav a { color: var(--ink); }
  .legal { position: absolute; left: 346px; top: 121px; color: var(--paper); font-size: 16.4px; line-height: 19px; }
  .support { position: absolute; left: 913px; top: 121px; color: var(--paper); font-size: 16.4px; line-height: 19px; }
</style>
</head>
<body>
<div class="page">
  <div class="brand brand--dark"><span class="brand-mark"></span>Clip Harbor Partners</div>

  <div class="nav-band"></div>
  <nav>
    <a class="nav-item" style="left:239px" href="#">Home</a>
    <a class="nav-item" style="left:334px" href="#">About us</a>
    <a class="nav-item" style="left:430px" href="#">Services</a>
    <a class="nav-item" style="left:526px" href="#">VSS</a>
    <a class="nav-item" style="left:622px" href="#">Contact</a>
  </nav>

  <div class="video-player" aria-label="Video about video SEO">
    <svg width="225" height="140" viewBox="0 0 225 140"><polygon points="87,58 133,71 87,84 97,71" fill="#fff"/></svg>
    <div class="controls">
      <svg width="225" height="14" viewBox="0 0 225 14">
        <polygon points="6,3 12,7 6,11" fill="#333"/>
        <rect x="20" y="6" width="140" height="2" fill="#999"/>
        <circle cx="24" cy="7" r="3" fill="#666"/>
        <rect x="205" y="4" width="12" height="6" rx="2" fill="#333"/>
      </svg>
    </div>
  </div>

  <div class="search-showcase" role="img" aria-label="Zentrova and FlickBarn search results showing client video thumbnails on the first page"></div>

  <h1 class="tagline">BRINGING YOU THE TRAFFIC YOU WANT</h1>
  <p class="subhead">FIRST-RATE <span class="gold">FIRST PAGE VIDEO</span> LISTINGS</p>
  <p class="intro">Lorem ipsum dolor sit amet, consetetur sadipscing elitr, sed diam nonumy eirmod tempor invidunt ut labore et dolore magna aliquyam erat, sed diam voluptua. At vero eos et accusam et justo duo dolores et ea rebum. Stet clita kasd gubergren, no sea takimata sanctus est Lorem ipsum dolor sit amet. Lorem ipsum dolor sit amet, consetetur sadipscing elitr, sed diam nonumy eirmod tempor invidunt ut labore et dolore magna aliquyam erat, sed diam voluptua. At vero eos et accusam et justo duo dolores et ea rebum.</p>
  <div class="rule"></div>

  <section class="benefits benefits--left">
    <h2>A Word or Two <span class="gold">About Your</span> Investment</h2>
    <ul>
      <li>Lorem ipsum dolor sit amet, consetetur sadipscing</li>
      <li>At vero eos et accusam et justo duo dolores et ea rebum. Stet clita kasd gubergren, no sea takimata</li>
      <li>At vero eos et accusam et justo duo dolores et ea rebum.</li>
      <li>Ipsum dolor sit amet, consetetur sadipscing elitr.</li>
    </ul>
  </section>
  <div class="divider"></div>
  <section class="benefits benefits--right">
    <h2>You Can Get a Lot <span class="gold">More Traffic</span> And SALES</h2>
    <ul>
      <li>Lorem ipsum dolor sit amet, consetetur sadipscing</li>
      <li>At vero eos et accusam et justo duo dolores et ea rebum. Stet clita kasd gubergren, no sea takimata</li>
      <li>At vero eos et accusam et justo duo dolores et ea rebum.</li>
      <li>Ipsum dolor sit amet, consetetur sadipscing elitr.</li>
    </ul>
  </section>

  <div class="client-tile" style="left:241px">Lumora</div>
  <div class="client-tile" style="left:395px">Paynix</div>
  <div class="client-tile" style="left:549px">Cardwell</div>
  <div class="client-tile" style="left:703px">Petrova</div>

  <div class="cta-band"></div>
  <div class="brand brand--light"><span class="brand-mark"></span>Clip Harbor Partners</div>
  <a class="cta">
    <svg width="20" height="20" viewBox="0 0 20 20"><polygon points="0,0 20,10 0,20 5,10" fill="#000"/></svg>
    REQUEST FREE VIDEO SEO CONSULT
    <svg width="20" height="20" viewBox="0 0 20 20"><polygon points="20,0 0,10 20,20 15,10" fill="#000"/></svg>
  </a>

  <footer class="footer">
    <div class="partner-list">
      <span>Cardwell</span><span>Lumora</span><span>Vantor Pay</span>
      <span>Paynix</span><span>Petrova</span><span>Grill Crown</span>
    </div>
    <nav class="footer-nav">
      <a href="#">Home</a><a href="#">About us</a><a href="#">Services</a><a href="#">VSS</a><a href="#">Contact</a>
    </nav>
    <p class="legal">© Plumfield Reels, LLC. - All Rights Reserved<br>Trademarks on this page are the property of their respective owners.</p>
    <p class="support">SUPPORT<br>800-555-0142</p>
  </footer>
</div>
</body>
</html>
```